KORBALT

The business want a professional looking business card. We have a scetch we will add but want the extra upgrade, and would like more suggestions for variations of our business cards.

```html
<!DOCTYPE html>
<html lang="en">
<head>
<meta charset="utf-8">
<title>KORBALT business card</title>
<link rel="stylesheet" href="https://fonts.googleapis.com/css2?family=Marcellus&family=Outfit:wght@300&display=swap">
<style>
  :root {
    --page: #ffffff;
    --card-center: #35220f;
    --card-edge: #22150f;
    --gold: #a98a45;
    --gold-bright: #e2bb62;
    --cream: #d8c79c;
  }
  * { margin: 0; padding: 0; box-sizing: border-box; }
  html, body {
    width: 1200px; height: 1200px; overflow: hidden;
    background: var(--page);
  }
  .canvas { position: relative; width: 1200px; height: 1200px; }
  .card {
    position: absolute;
    left: 290px; width: 627px; height: 358px;
    background: radial-gradient(ellipse at 50% 52%, var(--card-center) 0%, var(--card-edge) 75%);
    overflow: hidden;
  }
  .card--front { top: 207px; }
  .card--back { top: 643px; }

  .brand-mark {
    position: absolute;
    width: 56px; height: 56px; border-radius: 50%;
    background: var(--gold-bright);
  }
  .card--front .brand-mark { left: 285px; top: 106px; }
  .card--back .brand-mark { left: 536px; top: 50px; width: 40px; height: 40px; }

  .wordmark {
    position: absolute;
    font-family: "Marcellus", serif;
    font-weight: 400;
    line-height: 1;
    white-space: nowrap;
    letter-spacing: 0.02em;
  }
  .card--front .wordmark {
    left: 0; right: 0; top: 216px;
    text-align: center;
    font-size: 45px;
    color: var(--gold);
  }
  .card--back .wordmark {
    left: 45px; top: 68px;
    font-size: 35px;
    color: var(--cream);
  }

  .details {
    position: absolute; left: 45px; top: 106px;
    font-family: "Outfit", sans-serif;
    font-weight: 300;
    color: var(--cream);
    line-height: 1;
    white-space: nowrap;
  }
  .details .role { font-size: 37px; }
  .details .person { font-size: 22px; margin-top: 6px; letter-spacing: 0.02em; }
  .contact { list-style: none; margin-top: 42px; font-size: 20px; letter-spacing: 0.03em; }
  .contact li { height: 27.5px; }
</style>
</head>
<body>
<main class="canvas">
  <section class="card card--front">
    <div class="brand-mark" aria-hidden="true"></div>
    <h1 class="wordmark">KORBALT VESTLIND</h1>
  </section>

  <section class="card card--back">
    <div class="brand-mark" aria-hidden="true"></div>
    <h2 class="wordmark">KORBALT VESTLIND</h2>
    <div class="details">
      <p class="role">CEO &amp; Founder</p>
      <p class="person">Arne Olav Vestlind</p>
      <ul class="contact">
        <li>004791234567</li>
        <li>contact@korbalt.llc</li>
        <li>www.korbalt.llc</li>
      </ul>
    </div>
  </section>
</main>
</body>
</html>
```